Packiging of mouse trap

We need a packiging for a new mousetrap called 'The Snapwell'. It is a mouse/rat trap. We want to have it pretty simple and modern. The logo of the mouse trap is in the attachment and the measures of the packaging also (don't look at the design, it has nothing to do with us). It's needs to stand out in between the other packaging due to it's simplicity and modern touch.

Font styles to use
Sans Serif

Requirements
Must have
• Simplicity, modern
Should not have
• Too many colors

```html
<!DOCTYPE html>
<html lang="en">
<head>
<meta charset="UTF-8">
<title>The Snapwell – Mouse/Rat Trap Packaging</title>
<link href="https://fonts.googleapis.com/css2?family=Anton&family=Cormorant+Garamond:wght@500;600&display=swap" rel="stylesheet">
<style>
  :root {
    --backdrop: #dcd8d9;
    --ink: #0b0b0b;
    --paper: #ffffff;
    --paper-shade: #eeeeee;
    --reverse: #f4f4f4;
  }
  * { box-sizing: border-box; margin: 0; padding: 0; }
  html, body {
    width: 1200px;
    height: 1200px;
    overflow: hidden;
    background: var(--backdrop);
  }
  .dieline {
    position: absolute;
    left: 290px;
    top: 150px;
    display: flex;
    height: 900px;
  }
  .side-panel {
    position: relative;
    width: 210px;
    height: 100%;
    background: var(--ink);
  }
  .side-panel .outline-art {
    position: absolute;
    left: 30px;
    top: 220px;
    width: 110px;
    height: 380px;
    background: #1c1c1c;
  }
  .front-panel {
    position: relative;
    width: 410px;
    height: 100%;
    background: linear-gradient(90deg, var(--paper-shade) 0%, var(--paper) 30%, var(--paper) 100%);
    overflow: hidden;
  }
  .brand-name {
    position: absolute;
    top: 95px;
    left: 0;
    right: 0;
    text-align: center;
    font-family: "Anton", sans-serif;
    font-size: 74px;
    line-height: 0.92;
    color: var(--ink);
    text-transform: uppercase;
    letter-spacing: -1px;
  }
  .product-type {
    position: absolute;
    top: 445px;
    left: 0;
    right: 0;
    text-align: center;
    font-family: "Cormorant Garamond", serif;
    font-weight: 600;
    font-size: 34px;
    letter-spacing: 6px;
    line-height: 1.6;
    color: var(--ink);
  }
  .base-wave {
    position: absolute;
    left: 0;
    bottom: 0;
    width: 100%;
    height: 340px;
  }
  .rodent-art {
    position: absolute;
    left: 95px;
    top: 660px;
    width: 250px;
    height: 115px;
    background: #161616;
    border-radius: 50% 50% 10px 10px;
  }
  .spec-list {
    position: absolute;
    left: 18px;
    bottom: 26px;
    list-style: none;
    font-family: "Cormorant Garamond", serif;
    font-weight: 500;
    font-size: 17px;
    line-height: 1.45;
    color: var(--reverse);
  }
  .spec-list li::before {
    content: "\25C6";
    font-size: 8px;
    margin-right: 8px;
    vertical-align: 3px;
  }
</style>
</head>
<body>
  <main class="dieline">
    <section class="side-panel">
      <div class="outline-art" role="img" aria-label="Thin white line drawing of a rat seen from above"></div>
    </section>
    <section class="front-panel">
      <h1 class="brand-name">The<br>Snapwell</h1>
      <p class="product-type">MOUSE\RAT<br>TRAP</p>
      <svg class="base-wave" viewBox="0 0 410 340" preserveAspectRatio="none" aria-hidden="true">
        <path d="M0 40 C 60 60, 140 70, 230 70 C 310 70, 370 45, 410 20 L410 340 L0 340 Z" fill="#0b0b0b"/>
      </svg>
      <div class="rodent-art" role="img" aria-label="Black rat silhouette with a white outline and long curling tail"></div>
      <ul class="spec-list">
        <li>The Snapwell</li>
        <li>Electronic Rat Trap</li>
        <li>www.thesnapwell.com</li>
        <li>Model No : 000000 | Est.No : 000.0000-0000</li>
      </ul>
    </section>
  </main>
</body>
</html>
```